Wine Lable

We Are Moralba Ridge Wines and we are designing a new bottle for our top end wine named "The Velvet Harvest" I no exactly how i want the label to look and im searching for a talented designer to out my vision to life.

There will be 3 parts to this design.

Top Cover design with gold text wrapped around saying"The Velvet Harvest" (See Fig 2)

The front label which i want same as attached (See fig 2)

The Rear label
(See Fig 2 for design)
(See Fig 3 for content)

and final bottle design how it will look together
Updates

Come on guys keep the designs coming

Project Deadline Extended
Reason: I have extended my deadline due to the break from work over the Christmas new year period. Extra consideration will be made

Target Market(s)

The High End wine consumers the bottle cost will be $100USD

Font styles to use
Decorative
Script

Requirements
Must have

• Top Cover design with gold text wrapped around saying"The Velvet Harvest" (See Fig 2)
Black Rear Label with information and company name (Layout Fig 2) (Content Fig 3)
Gold and Black theme
The Text "Wine of Australia" somewhere on the bottle

```html
<!DOCTYPE html>
<html lang="en">
<head>
<meta charset="utf-8">
<title>The Velvet Harvest – Label Set</title>
<link href="https://fonts.googleapis.com/css2?family=Audiowide&family=Source+Sans+3:wght@400;600&display=swap" rel="stylesheet">
<style>
  :root {
    --ink: #000000;
    --paper: #ffffff;
    --gold-deep: #9a7a10;
    --gold-mid: #d4ad1e;
    --gold-light: #f4e6a8;
    --gold-text: #e2bc2c;
    --text-light: #ffffff;
  }
  * { margin: 0; padding: 0; box-sizing: border-box; }
  html, body {
    width: 1200px;
    height: 900px;
    overflow: hidden;
    background: var(--paper);
  }
  .canvas {
    position: relative;
    width: 1200px;
    height: 900px;
    font-family: "Source Sans 3", "Myriad Pro", Arial, sans-serif;
  }

  /* Shared title lettering */
  .wine-title {
    font-family: "Audiowide", "Arial Black", sans-serif;
    font-weight: 400;
    text-transform: uppercase;
    text-align: center;
    line-height: 1;
    letter-spacing: 0.02em;
  }
  .wine-title span { display: block; }

  /* Capsule band */
  .capsule-band {
    position: absolute;
    left: 352px; top: 68px;
    width: 503px; height: 100px;
    background: linear-gradient(90deg, var(--gold-light) 0%, var(--gold-mid) 20%, var(--gold-deep) 45%, var(--gold-mid) 60%, var(--gold-light) 80%, var(--gold-mid) 100%);
  }
  .capsule-band__title {
    position: absolute;
    left: 168px; top: 6px;
    width: 168px; height: 88px;
    background: var(--ink);
    color: var(--gold-text);
    display: flex;
    flex-direction: column;
    justify-content: center;
    font-size: 20px;
    line-height: 1.1;
  }
  .capsule-band__title .wine-title__the { font-size: 14px; }

  /* Front label */
  .front-label {
    position: absolute;
    left: 85px; top: 246px;
    width: 312px; height: 503px;
    background: var(--ink);
    padding: 10px 9px;
  }
  .front-label__artwork {
    position: relative;
    width: 100%; height: 100%;
    background: linear-gradient(90deg, var(--gold-deep) 0%, var(--gold-mid) 25%, var(--gold-light) 50%, var(--gold-mid) 75%, var(--gold-deep) 100%);
  }
  .front-label__title {
    position: absolute;
    left: 14px; top: 112px;
    width: 266px; height: 142px;
    background: var(--ink);
    color: var(--gold-text);
    display: flex;
    flex-direction: column;
    justify-content: center;
    font-size: 38px;
    line-height: 1.08;
  }
  .front-label__title .wine-title__the { font-size: 26px; }
  .front-label__origin {
    display: block;
    margin-top: 6px;
    font-size: 10px;
    letter-spacing: 0.2em;
  }

  /* Rear label */
  .rear-label {
    position: absolute;
    left: 500px; top: 272px;
    width: 207px; height: 449px;
    background: var(--ink);
    padding: 9px 9px;
  }
  .rear-label__foil {
    position: relative;
    width: 100%; height: 100%;
    background: linear-gradient(90deg, var(--gold-mid) 0%, var(--gold-light) 35%, var(--gold-mid) 55%, var(--gold-deep) 100%);
  }
  .rear-label__panel {
    position: absolute;
    left: 21px; top: 151px;
    width: 150px; height: 268px;
    background: var(--ink);
    color: var(--text-light);
    padding: 10px 8px 0;
    font-size: 6.2px;
    line-height: 1.3;
  }
  .rear-label__winery {
    text-align: center;
    font-size: 9.5px;
    margin-bottom: 10px;
  }
  .rear-label__notes {
    text-align: justify;
    margin-bottom: 8px;
  }
  .rear-label__producer,
  .rear-label__facts { margin-bottom: 8px; }
  .rear-label__code-space {
    position: absolute;
    left: 15px; top: 214px;
    width: 119px; height: 42px;
    background: var(--paper);
  }

  /* Monochrome label */
  .mono-label {
    position: absolute;
    left: 865px; top: 254px;
    width: 293px; height: 487px;
    background: var(--ink);
    padding: 8px 7px;
  }
  .mono-label__artwork {
    position: relative;
    width: 100%; height: 100%;
    background: linear-gradient(180deg, #6b6b6b 0%, #8a8a8a 50%, #6b6b6b 100%);
  }
  .mono-label__title {
    position: absolute;
    left: 10px; top: 112px;
    width: 259px; height: 134px;
    background: var(--paper);
    color: var(--ink);
    display: flex;
    flex-direction: column;
    justify-content: center;
    font-size: 38px;
    line-height: 1.08;
  }
  .mono-label__title .wine-title__the { font-size: 26px; }
</style>
</head>
<body>
<main class="canvas">
  <div class="capsule-band" role="img" aria-label="Gold and black maze pattern capsule band">
    <h2 class="capsule-band__title wine-title">
      <span class="wine-title__the">The</span>
      <span>Velvet</span>
      <span>Harvest</span>
    </h2>
  </div>

  <div class="front-label">
    <div class="front-label__artwork" role="img" aria-label="Gold foil maze pattern front label">
      <h1 class="front-label__title wine-title">
        <span class="wine-title__the">The</span>
        <span>Velvet</span>
        <span>Harvest</span>
        <span class="front-label__origin">Wine of Australia</span>
      </h1>
    </div>
  </div>

  <div class="rear-label">
    <div class="rear-label__foil">
      <div class="rear-label__panel">
        <p class="rear-label__winery">Moralba Ridge Wines</p>
        <p class="rear-label__notes">Deep, vibrant crimson/garnet colour. Blackcurrant and plum aromas with lifted clove-like spice complemented by toasty oak and a touch of fennel. Intense but balanced juicy red currant and plum characters on the palate with a gentle spice. Generous, soft mouth-filling tannins and balanced acidity.</p>
        <p class="rear-label__producer">Produced by: Copperleaf Cellars Australia<br>Unit 4, 212 Hillcrest Road<br>Kingsvale 5091<br>South Australia, Australia</p>
        <p class="rear-label__facts">Net Content 750ml<br>Alcohol Strength 15.5%<br>Approx 9.1 Standard Drinks<br>Contains Sulphite</p>
        <div class="rear-label__code-space"></div>
      </div>
    </div>
  </div>

  <div class="mono-label">
    <div class="mono-label__artwork" role="img" aria-label="Black and white maze pattern label">
      <h2 class="mono-label__title wine-title">
        <span class="wine-title__the">The</span>
        <span>Velvet</span>
        <span>Harvest</span>
      </h2>
    </div>
  </div>
</main>
</body>
</html>
```